We need a design for our website called Trocadim which is a brazilian e-commerce focused on childrenswear. Basically your are able to swap (sell & buy) your kids outgrown clothes in the website and we will offer all the necessary services to help you on that.

We believe the main characteristic of the company is the swap of clothes and accessories, but we also feel that by doing this we are guaranteeing that this clothes are not going to trash, reducing clothes waste and being friendly with the environment.

We believe it should be clean with solid and soft colors (refer to the logo attached) and should communicate high quality standards and trust.

We need 2 web pages: home/search results and product details. In both pages we would like to have a fixed top bar with the logo, menu (Buy, Sell, About Us), login, a short message and shopping cart. As well as a footer on the botton with different options and social network links.

- Home/search results: right at the beginning of the page we would like to have a welcome/explanatory carousel banner. It should be a conventional 2 columns design with filters on the left (~25%) and the results on the main section (~3/4 products per row). We need filters for clothes and accessories (size,category, brands, color, gender).

- Product details: again, this should be very clean, with breadcrumbs on the top, a very short description (product's name, category, size), price, "Add to cart" button, an image with zoom functionality (as reference: brisk lupex), a "Similar Items" box and a share bar (chatterbook, tweeplr, boardlyx, k+).

Please bear in mind that we plan to use the main template in different colors across the website.
Updates

Hi everyone! 

We have just updated the brief to add some "Must have features" and "Nice to have features". Please take a careful look at it as it affects pretty much every design we received so far.

We will guarantee the project in the next 1-2 days, but we first would like to see some initial proposals for the second page (product details). Some of you guys are doing an awesome job in the home page!

Best,

Trocadim team

We have just updated the contest payment status: it is now committed!

Best,
Trocadim Team

Target Market(s)

The main audience will be parents of any age

Industry/Entity Type

E-Commerce

Requirements
Must have
• We would like to have only the following elements in the header: logo, login, cart image, Home, "Compre" (Buy), "Venda" (Sell) - not necessarily in this order
- The header should be persistent all over the website (always fixed at the top), thus, if it is too thick it will end up eating too much vertical space in some pages
- The current page should be somehow highlited in the header
- Right next to the cart image on the top we need a small tag indicating how many itens are already inside the cart
- We need a button "Entenda como funcionamos" (which in english means "Learn more") in the banner
- Please use an image of childrens in the banner (not clothes or teenagers)
- Besides the banner, the user in a1024x768 screen resolution should at least be able to view the first row of search results
- There is no need for a "Add to cart" button in every search result (keep price, size, type only). This option should only be available in the second page (product details)
- When needed use "Adicionar ao carrinho" (portuguese) instead of "Add to cart" (english)
- Regarding social network links in the footer, we only need chatterbook, tweeplr, boardlyx, k+
- In the search results page we need an option to show 12, 24, 48 results per page
- Users need to be able to sort the results (newest first, price low-high and high-low)
Nice to have
• We don´t need a text search box anywhere in the website
- There is no need to present the payment methods in neither pages
- The image of the cart should be modified when there are items inside (full vs empty)
- When the user moves the mouse over the cart image, a simple "div" should show up bellow it listing all items
- Regarding social network links, we like icons that change colors when the user
moves the mouse over them
- Regarding the color scheme, use up to a max of 3 colors and feel free to change the logo colors if you find a better combination than the ones we provided

```html
<!DOCTYPE html>
<html lang="en">
<head>
<meta charset="utf-8">
<title>Trocadim – Home</title>
<link href="https://fonts.googleapis.com/css2?family=Lato:wght@300;400;700&display=swap" rel="stylesheet">
<style>
  :root{
    --brand:#6dcbe3;
    --brand-deep:#4fbcd8;
    --brand-soft:#9fdcec;
    --text:#8a8a8a;
    --line:#d6d6d6;
    --white:#ffffff;
  }
  *{box-sizing:border-box;margin:0;padding:0}
  html,body{width:1200px;height:1101px;overflow:hidden;background:var(--white);font-family:'Lato',sans-serif;color:var(--text)}
  .page{position:relative;width:1200px;height:1101px}

  /* header */
  .topbar{position:absolute;left:0;top:0;width:1200px;height:66px;background:linear-gradient(#ffffff,#f1f1f1);border-bottom:1px solid #e2e2e2;z-index:2}
  .logo{position:absolute;font-family:'Lato',sans-serif;font-weight:300;color:var(--brand);white-space:nowrap}
  .topbar .logo{left:125px;top:6px;font-size:44px;letter-spacing:1px}
  .nav a{position:absolute;top:22px;font-size:18px;font-weight:300;color:#8f8f8f;text-decoration:none}
  .nav a.current{color:var(--brand);font-weight:400}
  .hbtn{position:absolute;top:17px;height:32px;border:1px solid #cfcfcf;border-radius:3px;background:#fff;font-size:16px;font-weight:300;color:#8a8a8a;display:flex;align-items:center;gap:4px;padding:0 8px;white-space:nowrap}
  .hbtn.login{left:871px;width:74px}
  .hbtn.cart{left:947px;width:131px}
  .hbtn.cart b{color:var(--brand);font-weight:400}

  /* banner */
  .banner{position:absolute;left:0;top:66px;width:1200px;height:310px;background:linear-gradient(#8fd6ea 0%,#b9e6f2 55%,#ffffff 100%)}
  .banner-photo{position:absolute;left:136px;top:28px;width:422px;height:276px;border-radius:4px;background:linear-gradient(135deg,#f2c55a 0%,#d8455b 35%,#6fa5d6 70%,#e5e5e5 100%);opacity:.85}
  .welcome{position:absolute;left:550px;top:62px;width:506px;display:flex;flex-direction:column;align-items:center;text-align:center}
  .welcome h1{font-size:47px;font-weight:700;color:#fff;line-height:50px;margin-bottom:4px;white-space:nowrap}
  .welcome p{width:484px;font-size:18.5px;font-weight:300;color:#7c7c7c;line-height:25px}
  .learn{margin-top:4px;width:225px;height:32px;border-radius:3px;background:linear-gradient(#7fd3e8,#55bfd9);border:1px solid #4bb5d0;color:#fff;font-size:16px;font-weight:400;display:flex;align-items:center;justify-content:center}

  /* sort controls */
  .sort{position:absolute;top:376px;height:32px;border:1px solid #cfcfcf;border-radius:3px;background:#fff;color:var(--brand);font-size:17px;display:flex;align-items:center;justify-content:center;gap:7px;white-space:nowrap}
  .sort.show{left:840px;width:93px}
  .sort.newest{left:937px;width:130px}

  /* filters */
  .filters{position:absolute;left:129px;top:415px;width:155px;height:281px;background:var(--brand);border:1px solid #5fc2dc;border-radius:2px}
  .filters h2{position:absolute;left:16px;top:20px;font-size:23px;font-weight:700;color:#fff;letter-spacing:-.5px}
  .filters ul{list-style:none;position:absolute;left:0;top:73px;width:155px}
  .filters li{height:28px;line-height:28px;text-align:center;color:#fff;font-size:18px;font-weight:300}
  .filters li.active{width:127px;height:33px;line-height:36px;margin-bottom:-1px;background:#fff;color:var(--brand);border-radius:0 3px 3px 0;font-size:19px}

  /* product cards */
  .card{position:absolute;width:239px;height:280px;border:1px solid var(--line);border-radius:2px;background:#fff;text-align:center}
  .card .shot{position:absolute;left:20px;top:16px;width:199px;height:180px;border-radius:18px}
  .shot.yellow{background:radial-gradient(closest-side,#c7b21e 0%,#b59f12 94%,rgba(255,255,255,0) 100%)}
  .shot.cream{background:radial-gradient(closest-side,#f6f1d6 0%,#ece5c2 94%,rgba(255,255,255,0) 100%)}
  .shot.pink{background:radial-gradient(closest-side,#e6a8d9 0%,#d796cb 94%,rgba(255,255,255,0) 100%)}
  .shot.blue{background:radial-gradient(closest-side,#2d97c8 0%,#1f86b9 94%,rgba(255,255,255,0) 100%)}
  .card h3{position:absolute;left:0;right:0;top:201px;font-size:22px;color:var(--brand);letter-spacing:-.5px;white-space:nowrap}
  .card h3 b{font-weight:700}
  .card h3 i{font-weight:300;font-style:italic}
  .card .size{position:absolute;left:0;right:0;top:229px;font-size:17px;font-weight:300;color:#8a8a8a;white-space:nowrap}
  .card .price{position:absolute;left:0;right:42px;top:251px;font-size:18px;font-weight:300;color:var(--brand-soft);white-space:nowrap}
  .card .price b{font-weight:700;color:var(--brand)}
  .card .tools{position:absolute;right:10px;top:253px;display:flex;gap:4px}
  .card.best{width:196px}
  .card.best .label{position:absolute;left:0;right:0;top:6px;font-size:33px;color:var(--brand);letter-spacing:-.5px;white-space:nowrap}
  .card.best .label b{font-weight:700}
  .card.best .label i{font-weight:300;font-style:normal}
  .card.best .shot{left:20px;top:58px;width:156px;height:140px}
  .card.best .price{right:52px}
  .card.best .tools{right:6px}

  /* footer */
  .footer{position:absolute;left:0;top:1034px;width:1200px;height:67px;background:linear-gradient(#f7f7f7,#e9e9e9);border-top:1px solid #e1e1e1}
  .follow{position:absolute;left:143px;top:24px;font-size:18px;font-weight:300;color:#7d7d7d}
  .social{position:absolute;left:230px;top:26px;display:flex;gap:8px;list-style:none}
  .social li{display:flex;align-items:center;gap:4px;font-size:12px;color:var(--brand-deep)}
  .social li span.sq{width:14px;height:14px;background:var(--brand);border-radius:2px}
  .footer .logo{right:134px;top:12px;font-size:36px;color:#9a9a9a}
</style>
</head>
<body>
<div class="page">

  <header class="topbar">
    <div class="logo">Trocadim</div>
    <nav class="nav">
      <a class="current" style="left:467px">Home</a>
      <a style="left:567px">Compre</a>
      <a style="left:682px">Venda</a>
    </nav>
    <div class="hbtn login">
      <svg width="12" height="14" viewBox="0 0 12 14"><rect x="1" y="6" width="10" height="8" rx="1" fill="var(--brand)"/><path d="M3 6V4a3 3 0 0 1 6 0v2" fill="none" stroke="var(--brand)" stroke-width="2"/></svg>
      Login
    </div>
    <div class="hbtn cart">
      <svg width="24" height="18" viewBox="0 0 24 18"><path d="M1 2h4l3 10h12l3-8H7" fill="none" stroke="var(--brand)" stroke-width="2"/><rect x="8" y="5" width="13" height="5" fill="var(--brand-soft)"/><circle cx="9" cy="16" r="1.6" fill="var(--brand)"/><circle cx="19" cy="16" r="1.6" fill="var(--brand)"/></svg>
      <b>2</b> products
    </div>
  </header>

  <section class="banner">
    <div class="banner-photo" role="img" aria-label="Photo of a group of happy children jumping in colourful clothes"></div>
    <div class="welcome">
      <h1>Welcome to Trocadim</h1>
      <p>Lorem ipsum dolor sit amet, consectetur adipiscing elit. Praesent et odio eu nisi porta pulvinar. Donec quam massa, sollicitudin vitae venenatis vitae, blandit nec magna. In lobortis, metus a fringilla euismod, leo nulla luctus dolor</p>
      <div class="learn">Entenda como funcionamos</div>
    </div>
  </section>

  <div class="sort show">
    <svg width="15" height="15" viewBox="0 0 16 16"><circle cx="8" cy="8" r="8" fill="#8f8f8f"/><path d="M8 4v6M5 8l3 3 3-3" stroke="#fff" stroke-width="2" fill="none"/></svg>show
  </div>
  <div class="sort newest">
    <svg width="15" height="15" viewBox="0 0 16 16"><circle cx="8" cy="8" r="8" fill="#8f8f8f"/><path d="M8 4v6M5 8l3 3 3-3" stroke="#fff" stroke-width="2" fill="none"/></svg>newest first
  </div>

  <aside class="filters">
    <h2>PRODUCTS</h2>
    <ul>
      <li class="active">All</li>
      <li>Size</li>
      <li>Category</li>
      <li>Brands</li>
      <li>Color</li>
      <li>Gender</li>
    </ul>
  </aside>

  <svg width="0" height="0" style="position:absolute">
    <defs>
      <g id="eye"><path d="M1 7C5 1 15 1 19 7C15 13 5 13 1 7Z" fill="none" stroke="#8a8a8a" stroke-width="1.6"/><circle cx="10" cy="7" r="3" fill="#8a8a8a"/></g>
      <g id="zoom"><circle cx="7" cy="7" r="5" fill="none" stroke="#8a8a8a" stroke-width="2.2"/><path d="M11 11l5 5" stroke="#8a8a8a" stroke-width="2.6"/></g>
    </defs>
  </svg>

  <article class="card" style="left:331px;top:415px">
    <div class="shot yellow" role="img" aria-label="Photo of a mustard yellow kids t-shirt with a surf print"></div>
    <h3><b>T-Shirt</b> <i>YellowSurf</i></h3>
    <div class="size">Size: -XXS-XS-S-M</div>
    <div class="price">Price / <b>$15</b></div>
    <div class="tools"><svg width="20" height="14"><use href="#eye"/></svg><svg width="17" height="17"><use href="#zoom"/></svg></div>
  </article>
  <article class="card" style="left:584px;top:415px">
    <div class="shot cream" role="img" aria-label="Photo of a cream kids t-shirt with a bird print"></div>
    <h3><b>T-Shirt</b> <i>Follow@you</i></h3>
    <div class="size">Size: -XXS-XS-S-M</div>
    <div class="price">Price / <b>$12</b></div>
    <div class="tools"><svg width="20" height="14"><use href="#eye"/></svg><svg width="17" height="17"><use href="#zoom"/></svg></div>
  </article>
  <article class="card" style="left:837px;top:415px">
    <div class="shot pink" role="img" aria-label="Photo of a pink kids t-shirt with a surf print"></div>
    <h3><b>T-Shirt</b> <i>Follow@you</i></h3>
    <div class="size">Size: -XXS-XS-S-M</div>
    <div class="price">Price / <b>$12</b></div>
    <div class="tools"><svg width="20" height="14"><use href="#eye"/></svg><svg width="17" height="17"><use href="#zoom"/></svg></div>
  </article>

  <article class="card best" style="left:119px;top:712px">
    <div class="label"><b>Best</b> <i>Seller</i></div>
    <div class="shot blue" role="img" aria-label="Photo of a blue kids t-shirt with a surf print"></div>
    <h3><b>T-Shirt</b> <i>BlueSurf</i></h3>
    <div class="size">Size: -XXS-XS-S-M</div>
    <div class="price">Price / <b>$15</b></div>
    <div class="tools"><svg width="20" height="14"><use href="#eye"/></svg><svg width="17" height="17"><use href="#zoom"/></svg></div>
  </article>
  <article class="card" style="left:331px;top:712px">
    <div class="shot yellow" role="img" aria-label="Photo of a mustard yellow kids t-shirt with a surf print"></div>
    <h3><b>T-Shirt</b> <i>YellowSurf</i></h3>
    <div class="size">Size: -XXS-XS-S-M</div>
    <div class="price">Price / <b>$15</b></div>
    <div class="tools"><svg width="20" height="14"><use href="#eye"/></svg><svg width="17" height="17"><use href="#zoom"/></svg></div>
  </article>
  <article class="card" style="left:584px;top:712px">
    <div class="shot cream" role="img" aria-label="Photo of a cream kids t-shirt with a bird print"></div>
    <h3><b>T-Shirt</b> <i>Follow@you</i></h3>
    <div class="size">Size: -XXS-XS-S-M</div>
    <div class="price">Price / <b>$12</b></div>
    <div class="tools"><svg width="20" height="14"><use href="#eye"/></svg><svg width="17" height="17"><use href="#zoom"/></svg></div>
  </article>
  <article class="card" style="left:837px;top:712px">
    <div class="shot pink" role="img" aria-label="Photo of a pink kids t-shirt with a surf print"></div>
    <h3><b>T-Shirt</b> <i>Follow@you</i></h3>
    <div class="size">Size: -XXS-XS-S-M</div>
    <div class="price">Price / <b>$12</b></div>
    <div class="tools"><svg width="20" height="14"><use href="#eye"/></svg><svg width="17" height="17"><use href="#zoom"/></svg></div>
  </article>

  <footer class="footer">
    <div class="follow">Follow us</div>
    <ul class="social">
      <li><span class="sq"></span>chatterbook</li>
      <li><span class="sq"></span>tweeplr</li>
      <li><span class="sq"></span>k+</li>
      <li><span class="sq"></span>boardlyx</li>
    </ul>
    <div class="logo">Trocadim</div>
  </footer>

</div>
</body>
</html>
```